IT company requires website redesign

I have an old boring website that I want to update - www.tvkb-example.net
I am a growing IT company beginning to look after more healthcare professionals such as medical and dental practices so a more professional look is required

Blue and orange are the company colours. See one of our local competitors for your reference and ideas - https://www.plinth-halvard.example.au

Target Market(s)

Medical, dental, professional, solicitors etc

Industry/Entity Type

It Support

Number of Pages Required

5+ page

Colors

Designer to choose colors to be used in the design.

Requirements
Must have
• Classy feel, simple with the 'less is more' approach
• On support page, links to support items, a couple more to come
• Reference to our technology partners
• Easy to read
Nice to have
• Company colours are blue with a little orange but I willing to consider new web colour schemes
• leave the rest to you

```html
<!DOCTYPE html>
<html lang="en">
<head>
<meta charset="utf-8">
<title>Corvane Systems — Home</title>
<link rel="stylesheet" href="https://fonts.googleapis.com/css2?family=Jost:wght@400;500&family=Arimo:wght@400&family=Open+Sans:wght@400&display=swap">
<style>
  :root {
    --brand-blue: #1f3f9e;
    --brand-orange: #ee5a1f;
    --ink: #1a1a1a;
    --body-text: #333333;
    --nav-text: #222222;
    --page-bg: #ffffff;
    --hero-light: #f3f7fa;
    --hero-mid: #d6e2ea;
    --hero-deep: #b9cbd8;
  }
  * { margin: 0; padding: 0; box-sizing: border-box; }
  html, body { width: 1200px; height: 626px; overflow: hidden; background: var(--page-bg); }
  body { font-family: "Open Sans", Arial, sans-serif; color: var(--body-text); }

  .site { width: 1200px; height: 626px; position: relative; }

  .site-header {
    height: 68px; display: flex; align-items: center; justify-content: space-between;
    padding: 0 100px 0 130px;
  }
  .brand { display: flex; align-items: center; gap: 8px; font-family: "Jost", sans-serif; font-weight: 500; font-size: 19px; color: var(--brand-blue); }
  .brand-dot { width: 12px; height: 12px; border-radius: 50%; background: var(--brand-orange); }
  .main-nav { display: flex; gap: 32px; font-family: "Arimo", Arial, sans-serif; font-size: 12.5px; }
  .main-nav a { color: var(--nav-text); text-decoration: none; }
  .main-nav a.is-current { color: var(--brand-orange); }

  .hero { position: relative; height: 300px; }
  .hero-visual {
    position: absolute; inset: 0;
    background: linear-gradient(90deg, var(--hero-mid) 0%, var(--hero-light) 35%, var(--hero-light) 55%, var(--hero-deep) 78%, var(--hero-light) 100%);
  }
  .hero-copy { position: absolute; left: 125px; top: 92px; }
  .hero-title { font-family: "Jost", sans-serif; font-weight: 400; font-size: 34px; line-height: 1.08; color: var(--ink); letter-spacing: 0.3px; }
  .hero-tagline { font-family: "Jost", sans-serif; font-size: 16px; line-height: 1.3; color: var(--ink); margin-top: 10px; width: 300px; }

  .welcome { text-align: center; padding-top: 26px; }
  .welcome-title { font-family: "Jost", sans-serif; font-weight: 400; font-size: 24px; color: var(--ink); }
  .welcome-title .accent { color: var(--brand-orange); }
  .welcome-text { font-size: 11.5px; line-height: 1.55; width: 760px; margin: 10px auto 0; }
  .welcome-text + .welcome-text { margin-top: 8px; }

  .offerings { display: flex; justify-content: center; gap: 50px; margin-top: 16px; }
  .offering { width: 90px; height: 74px; display: flex; flex-direction: column; align-items: center; justify-content: center; gap: 6px; font-size: 10px; color: var(--body-text); }
  .offering.is-active { border: 1px solid var(--brand-orange); }
  .offering svg { width: 34px; height: 34px; }
</style>
</head>
<body>
<div class="site">
  <header class="site-header">
    <div class="brand"><span class="brand-dot"></span>Corvane Systems</div>
    <nav class="main-nav">
      <a class="is-current" href="#">Home</a>
      <a href="#">Our Services</a>
      <a href="#">About Us</a>
      <a href="#">Our Team</a>
      <a href="#">Contact Us</a>
      <a href="#">Support</a>
    </nav>
  </header>

  <section class="hero">
    <div class="hero-visual" role="img" aria-label="Photo of a doctor in a white coat with a stethoscope using a tablet in a bright glass-walled office"></div>
    <div class="hero-copy">
      <h1 class="hero-title">WELCOME TO CORVANE<br>SYSTEMS!</h1>
      <p class="hero-tagline">A Better Tomorrow, Through Intelligent use of Technology Today!</p>
    </div>
  </section>

  <section class="welcome">
    <h2 class="welcome-title">Welcome To Our <span class="accent">Website!</span></h2>
    <p class="welcome-text">Welcome to Corvane Systems where we believe that a better tomorrow, starts through intelligent use of technology today! Corvane Systems is a valued added information technology company supplying and implementing hardware and software that are complemented by the provision of associated support services and solutions.</p>
    <p class="welcome-text">We ensure that the risks associated with the deployment of new technologies are reduced, while providing a competitive total cost of IT ownership that yields a compelling return on investment.</p>

    <div class="offerings">
      <div class="offering">
        <svg viewBox="0 0 34 34" fill="none" stroke="var(--brand-blue)" stroke-width="2">
          <path d="M7 3h14l6 6v20H7z"/><path d="M21 3v6h6"/>
          <circle cx="17" cy="21" r="4"/><path d="M17 14v3M17 25v3M10 21h3M21 21h3"/>
        </svg>
        Software
      </div>
      <div class="offering is-active">
        <svg viewBox="0 0 34 34" fill="none" stroke="var(--brand-blue)" stroke-width="2" stroke-linejoin="round">
          <path d="M4 11l13-6 13 6-13 6z"/><path d="M4 11v13l13 6 13-6V11"/><path d="M17 17v13"/>
        </svg>
        Products
      </div>
      <div class="offering">
        <svg viewBox="0 0 34 34" fill="none" stroke="var(--brand-blue)" stroke-width="2">
          <circle cx="17" cy="17" r="6"/><circle cx="17" cy="17" r="2"/>
          <path d="M17 3v5M17 26v5M3 17h5M26 17h5M7 7l3.5 3.5M23.5 23.5L27 27M27 7l-3.5 3.5M10.5 23.5L7 27"/>
        </svg>
        Solutions
      </div>
    </div>
  </section>
</div>
</body>
</html>
```